Morvell Agronomics, Inc. Business Card

We are joint venture hybrid vegetable seed company. We design & breed application specific products for fresh market and processing applications. We are looking for a business card that will have impact and convey elegance, excellence, high technology, and have enormous eye appeal. It needs to be unique in design and can incorporate photos, or symbols as the case may be.

I very much enjoy the minimalist approach to Quorin's product designs. We would like to include a tag line in the business card: Breeding Success

Target Market(s)

We breed proprietary products that provide better solutions for growers, harvesters, packers, shippers, wholesalers, retailers, consumers, and processors. Regional seed distributors worldwide are our primary clients and then growers. We need to appeal first and foremost to the distributors who will be representing us and selling the products in their target markets.

Industry/Entity Type

Business

Requirements
Must have
• It will have a picture of a cluster of tomatoes on one side and the other side will include the logo, a tag line, our contact information, and a possibly a picture or symbol. I want the contact side to be edgy and convey elegance, solidity, and exclusivity.
Nice to have
• Surprise us with something special.
Should not have
• Card needs to work well with the green logo so it can't be diminished by the background color of the card.

```html
<!DOCTYPE html>
<html lang="en">
<head>
<meta charset="utf-8">
<title>Morvell Agronomics, Inc. – Business Card</title>
<link rel="stylesheet" href="https://fonts.googleapis.com/css2?family=Oswald:wght@300;400&family=Roboto+Slab:wght@100..900&display=swap">
<style>
  :root {
    --card-grey: #939598;
    --swirl-light: #b4b5b8;
    --photo-dark: #3c3c3c;
    --photo-mid: #8a8a8a;
    --photo-light: #c9c9c9;
    --tomato-red: #d8231c;
    --ink: #1f1d1e;
    --white: #ffffff;
    --soft-white: #d6d7d9;
    --dot-line: #6a6b6e;
    --frame-line: #d9d9d9;
  }
  html, body {
    margin: 0;
    padding: 0;
    width: 1200px;
    height: 343px;
    overflow: hidden;
    background: var(--white);
  }
  .card-spread {
    position: relative;
    width: 1200px;
    height: 343px;
    display: flex;
  }
  .card-front {
    position: relative;
    width: 600px;
    height: 343px;
    overflow: hidden;
  }
  .tomato-photo {
    position: absolute;
    inset: 0;
    background:
      radial-gradient(ellipse 130px 170px at 300px 175px, var(--tomato-red) 0%, rgba(216,35,28,0.85) 55%, rgba(216,35,28,0) 100%),
      linear-gradient(90deg, var(--photo-dark) 0%, var(--photo-mid) 35%, var(--photo-light) 55%, var(--photo-mid) 75%, var(--photo-dark) 100%);
  }
  .frame-lines {
    position: absolute;
    inset: 0;
  }
  .card-back {
    position: relative;
    width: 600px;
    height: 343px;
    background: var(--card-grey);
    overflow: hidden;
  }
  .swirl-area {
    position: absolute;
    left: 432px;
    top: 0;
    width: 168px;
    height: 343px;
    background: radial-gradient(ellipse 90px 160px at 110px 170px, var(--swirl-light) 0%, rgba(180,181,184,0) 100%);
  }
  .tagline {
    position: absolute;
    left: 34px;
    top: 44px;
    margin: 0;
    font-family: "Roboto Slab", "Rockwell", serif;
    line-height: 1;
  }
  .tagline-light {
    display: block;
    font-weight: 100;
    font-size: 92px;
    line-height: 92px;
    color: var(--white);
    letter-spacing: -1px;
  }
  .tagline-bold {
    display: block;
    font-weight: 900;
    font-size: 84px;
    line-height: 78px;
    color: var(--ink);
    margin-left: 50px;
    margin-top: -6px;
    letter-spacing: -2px;
  }
  .divider {
    position: absolute;
    left: 36px;
    top: 243px;
    width: 380px;
    height: 6px;
  }
  .contact-person {
    position: absolute;
    left: 38px;
    top: 256px;
    font-family: "Oswald", sans-serif;
  }
  .person-name {
    margin: 0;
    font-size: 12px;
    line-height: 15px;
    font-weight: 400;
    color: var(--ink);
  }
  .person-title {
    margin: 1px 0 0;
    font-size: 11px;
    line-height: 14px;
    font-weight: 300;
    color: var(--soft-white);
  }
  .contact-address {
    position: absolute;
    right: 184px;
    top: 254px;
    margin: 0;
    font-family: "Oswald", sans-serif;
    font-style: normal;
    font-size: 11.5px;
    font-weight: 300;
    line-height: 15px;
    text-align: right;
    color: var(--ink);
  }
  .contact-address .phone-line {
    color: var(--soft-white);
  }
  .brand-badge {
    position: absolute;
    left: 494px;
    top: 42px;
    width: 80px;
    height: 80px;
    border-radius: 50%;
    background: var(--white);
    display: flex;
    align-items: center;
    justify-content: center;
    text-align: center;
  }
  .brand-name {
    font-family: "Oswald", sans-serif;
    font-weight: 400;
    font-size: 10px;
    line-height: 12px;
    color: var(--ink);
  }
</style>
</head>
<body>
  <main class="card-spread">
    <section class="card-front">
      <div class="tomato-photo" role="img" aria-label="Photograph of a vine cluster of ripe red tomatoes against a soft grey greenhouse background"></div>
      <svg class="frame-lines" width="600" height="343" viewBox="0 0 600 343" aria-hidden="true">
        <polyline points="168,26 28,26 28,317 168,317" fill="none" stroke="var(--frame-line)" stroke-width="1.5"/>
        <polyline points="432,26 572,26 572,317 432,317" fill="none" stroke="var(--frame-line)" stroke-width="1.5"/>
      </svg>
    </section>

    <section class="card-back">
      <div class="swirl-area" role="img" aria-label="Decorative white spiral flourish curling down the right edge of the card"></div>

      <h1 class="tagline">
        <span class="tagline-light">Breeding</span>
        <span class="tagline-bold">Success</span>
      </h1>

      <svg class="divider" viewBox="0 0 380 6" aria-hidden="true">
        <line x1="3" y1="3" x2="377" y2="3" stroke="var(--dot-line)" stroke-width="1" stroke-dasharray="1 2"/>
        <circle cx="3" cy="3" r="2.2" fill="var(--dot-line)"/>
        <circle cx="377" cy="3" r="2.2" fill="var(--dot-line)"/>
      </svg>

      <div class="contact-person">
        <p class="person-name">DANIEL VASKER</p>
        <p class="person-title">Executing Manager</p>
      </div>

      <address class="contact-address">
        48 - ORCHARD LANE, B/12-GREENFIELD<br>
        TOWER 560021- PUNE, INDIA<br>
        <span class="phone-line">Ph. 002-31870649, Fax-002-31870650</span>
      </address>

      <div class="brand-badge">
        <span class="brand-name">Morvell<br>Agronomics, Inc.</span>
      </div>
    </section>
  </main>
</body>
</html>
```